VoxMend needs a Letterhead

We need a letterhead for our company "VoxMend Consultants". Logo is attached. The company color is Turquoise. Icons for website, scan logo for website, icons for address, e-mail and phone appreciated rather than just words.

Industry/Entity Type

It Company

```html
<!DOCTYPE html>
<html lang="en">
<head>
<meta charset="utf-8">
<title>VoxMend Consultants Letterhead</title>
<link rel="stylesheet" href="https://fonts.googleapis.com/css2?family=Merriweather:wght@400&family=Open+Sans:wght@600&display=swap">
<style>
  :root {
    --brand-blue: #1b7bbf;
    --brand-green: #8cc63f;
    --ink: #222222;
    --rule-blue: #9cc9e6;
    --rule-green: #c9e3a6;
    --footer-mark: #e3e3e3;
    --footer-text: #d6d6d6;
    --paper: #ffffff;
  }
  * { margin: 0; padding: 0; box-sizing: border-box; }
  html, body { width: 827px; height: 1200px; overflow: hidden; background: var(--paper); }
  .letterhead {
    position: relative;
    width: 827px;
    height: 1200px;
    background: var(--paper);
    font-family: "Merriweather", Georgia, serif;
    color: var(--ink);
  }
  .company-name {
    position: absolute;
    right: 262px;
    top: 2px;
    font-size: 32px;
    font-weight: 400;
    white-space: nowrap;
    letter-spacing: -0.2px;
  }
  .company-name .first { color: var(--brand-blue); }
  .company-name .second { color: var(--brand-green); }
  .contact-block, .address-block {
    position: absolute;
    right: 262px;
    text-align: right;
    font-size: 12.5px;
    line-height: 17px;
    white-space: nowrap;
  }
  .contact-block { top: 44px; }
  .address-block { top: 110px; }
  .header-rule {
    position: absolute;
    left: 164px;
    top: 96px;
    width: 401px;
    height: 1.5px;
    background: var(--rule-blue);
  }
  .header-divider {
    position: absolute;
    left: 585px;
    top: 0;
    width: 1.5px;
    height: 150px;
    background: var(--rule-green);
  }
  .brand-lockup {
    position: absolute;
    left: 622px;
    top: 20px;
    display: flex;
    align-items: center;
    gap: 12px;
  }
  .brand-square {
    width: 42px;
    height: 42px;
    background: var(--brand-blue);
  }
  .brand-word {
    font-family: "Open Sans", Arial, sans-serif;
    font-weight: 600;
    font-size: 27px;
    color: var(--brand-blue);
  }
  .footer-marks {
    position: absolute;
    left: 0;
    bottom: 8px;
    width: 827px;
    display: flex;
    justify-content: space-between;
    padding: 0 4px;
  }
  .footer-mark {
    display: flex;
    align-items: center;
    gap: 8px;
  }
  .footer-mark-square {
    width: 30px;
    height: 30px;
    background: var(--footer-mark);
  }
  .footer-mark-word {
    font-family: "Open Sans", Arial, sans-serif;
    font-weight: 600;
    font-size: 19px;
    color: var(--footer-text);
  }
</style>
</head>
<body>
<main class="letterhead">
  <header>
    <h1 class="company-name"><span class="first">VoxMend</span> <span class="second">Consultants</span></h1>
    <div class="contact-block">
      <p>www.voxmendconsultants.com</p>
      <p>E-mail : voxmendconsultants@mailbox.com</p>
      <p>Phone : +11 - 555012345</p>
    </div>
    <div class="header-rule"></div>
    <address class="address-block" style="font-style: normal;">
      <p># 500, Aaaaa Street, Address address</p>
      <p>address address addressaddress</p>
      <p>address address address address address</p>
    </address>
    <div class="header-divider"></div>
    <div class="brand-lockup">
      <span class="brand-square"></span>
      <span class="brand-word">VoxMend</span>
    </div>
  </header>

  <footer class="footer-marks">
    <div class="footer-mark"><span class="footer-mark-square"></span><span class="footer-mark-word">VoxMend</span></div>
    <div class="footer-mark"><span class="footer-mark-square"></span><span class="footer-mark-word">VoxMend</span></div>
    <div class="footer-mark"><span class="footer-mark-square"></span><span class="footer-mark-word">VoxMend</span></div>
    <div class="footer-mark"><span class="footer-mark-square"></span><span class="footer-mark-word">VoxMend</span></div>
    <div class="footer-mark"><span class="footer-mark-square"></span><span class="footer-mark-word">VoxMend</span></div>
  </footer>
</main>
</body>
</html>
```